Business card design needed

I need a business card for my Sydney Painting Business, that specialises in painting High -end residential homes. i want the design to look clean, modern and edgy. i also want a logo next to the RK Decorating, using RKD together.

Industry/Entity Type

Residential

Contact Information for Business Card

RK Decorating (business name),LIC 581062B, Rob Kellaway, robert.kellaway@fernmail.net, mobile 0412573068

```html
<!DOCTYPE html>
<html lang="en">
<head>
<meta charset="utf-8">
<title>RK Decorating – Business Card</title>
<link rel="stylesheet" href="https://fonts.googleapis.com/css2?family=Quicksand:wght@300;500;600&display=swap">
<style>
  :root {
    --sky: #0ab4e6;
    --sky-deep: #0a8fc9;
    --paper: #ffffff;
    --backdrop: #f3f4f5;
    --white: #ffffff;
    --warm-soft: #fbd08a;
    --coral-soft: #f7a0a8;
    --teal-soft: #8fd6c8;
  }
  * { margin: 0; padding: 0; box-sizing: border-box; }
  html, body {
    width: 1200px;
    height: 742px;
    overflow: hidden;
    background: var(--backdrop);
    font-family: "Quicksand", sans-serif;
  }
  .sheet {
    position: relative;
    width: 1200px;
    height: 742px;
  }
  .card {
    position: absolute;
    top: 224px;
    width: 560px;
    height: 293px;
    overflow: hidden;
    box-shadow: 0 2px 10px rgba(0, 0, 0, 0.08);
  }

  /* Front */
  .card--front { left: 30px; background: var(--paper); }
  .front__band {
    position: absolute;
    left: 0; top: 0;
    width: 16px; height: 100%;
    background: var(--sky);
  }
  .front__tagline {
    position: absolute;
    left: 36px; top: 42px;
    font-size: 12px;
    font-weight: 300;
    letter-spacing: 0.6px;
    color: var(--sky);
  }
  .front__artwork {
    position: absolute;
    left: 160px; top: 46px;
    width: 195px; height: 200px;
    background: linear-gradient(160deg, var(--coral-soft) 0%, var(--warm-soft) 50%, var(--teal-soft) 100%);
    opacity: 0.55;
  }
  .front__brand {
    position: absolute;
    left: 384px; top: 140px;
    display: flex;
    align-items: center;
    gap: 8px;
  }
  .brand__mark {
    width: 12px; height: 12px;
    flex: none;
    background: var(--sky);
  }
  .brand__name {
    font-size: 20px;
    font-weight: 600;
    line-height: 1.15;
    color: var(--sky);
  }

  /* Back */
  .card--back { left: 610px; background: var(--sky); }
  .back__pattern {
    position: absolute;
    right: 0; top: 0;
    width: 380px; height: 100%;
    background: linear-gradient(120deg, rgba(255,255,255,0) 10%, rgba(255,255,255,0.14) 45%, rgba(10,143,201,0.3) 75%, rgba(255,255,255,0.08) 100%);
  }
  .back__brand {
    position: absolute;
    left: 24px; top: 20px;
    font-size: 17px;
    font-weight: 600;
    line-height: 1.1;
    color: var(--white);
  }
  .back__name {
    position: absolute;
    left: 169px; top: 126px;
    font-size: 25px;
    font-weight: 500;
    letter-spacing: 0.5px;
    color: var(--white);
  }
  .back__contacts {
    position: absolute;
    left: 22px; bottom: 12px;
    list-style: none;
    font-size: 11.5px;
    font-weight: 500;
    line-height: 17px;
    color: var(--white);
  }
  .contact {
    display: flex;
    align-items: center;
    gap: 8px;
  }
  .contact__marker { width: 9px; height: 6px; flex: none; }
  .contact__key { width: 16px; }
</style>
</head>
<body>
<main class="sheet">
  <section class="card card--front" aria-label="Card front">
    <div class="front__band"></div>
    <p class="front__tagline">..painting world..</p>
    <div class="front__artwork" role="img" aria-label="Colourful geometric triangle artwork in blue, coral, yellow, orange and teal"></div>
    <div class="front__brand">
      <span class="brand__mark"></span>
      <p class="brand__name">RK<br>Decorating</p>
    </div>
  </section>

  <section class="card card--back" aria-label="Card back">
    <div class="back__pattern" role="img" aria-label="Faint overlapping translucent triangle pattern in light blue"></div>
    <p class="back__brand">RK<br>Decorating</p>
    <h1 class="back__name">rob kellaway</h1>
    <ul class="back__contacts">
      <li class="contact">
        <svg class="contact__marker" viewBox="0 0 9 6"><polygon points="0,0 9,0 4.5,6" fill="#ffffff"/></svg>
        <span class="contact__key">a</span><span>: LIC 581062B</span>
      </li>
      <li class="contact">
        <svg class="contact__marker" viewBox="0 0 9 6"><polygon points="0,0 9,0 4.5,6" fill="#ffffff"/></svg>
        <span class="contact__key">m</span><span>: 0412573068</span>
      </li>
      <li class="contact">
        <svg class="contact__marker" viewBox="0 0 9 6"><polygon points="0,0 9,0 4.5,6" fill="#ffffff"/></svg>
        <span class="contact__key">e</span><span>: robert.kellaway@fernmail.net</span>
      </li>
    </ul>
  </section>
</main>
</body>
</html>
```